KRT Design Business Card

I need to develop a business card for my real estate design and investment company. Something clean, classic and professional with a modern vibe.

Industry/Entity Type

Real Estate

Font styles to use
Serif
Sans Serif

```html
<!DOCTYPE html>
<html lang="en">
<head>
<meta charset="utf-8">
<title>KRT Design Business Card</title>
<link href="https://fonts.googleapis.com/css2?family=Open+Sans:wght@300;400;600;700&display=swap" rel="stylesheet">
<style>
  :root {
    --stage: #d6d6d6;
    --ink: #0b0b0b;
    --paper: #ffffff;
    --muted: #e6e6e6;
    --shadow: rgba(0, 0, 0, 0.28);
  }
  * { margin: 0; padding: 0; box-sizing: border-box; }
  html, body {
    width: 1200px;
    height: 900px;
    overflow: hidden;
    background: var(--stage);
    font-family: "Open Sans", Arial, sans-serif;
  }
  .stage { position: relative; width: 1200px; height: 900px; }
  .card {
    position: absolute;
    width: 520px;
    height: 300px;
    background: var(--ink);
    box-shadow: 0 10px 24px var(--shadow);
    overflow: hidden;
  }
  .card-front { left: 50px; top: 320px; }
  .card-back { left: 630px; top: 270px; }
  .card-shapes { position: absolute; inset: 0; }

  .front-brand {
    position: absolute;
    left: 24px;
    top: 96px;
    font-weight: 300;
    font-size: 30px;
    letter-spacing: 1px;
    color: var(--ink);
  }
  .holder-name {
    position: absolute;
    right: 62px;
    top: 48px;
    font-weight: 700;
    font-size: 27px;
    letter-spacing: 3px;
    color: var(--paper);
  }
  .holder-title {
    position: absolute;
    right: 62px;
    top: 88px;
    font-weight: 700;
    font-size: 14px;
    letter-spacing: 2.5px;
    color: var(--paper);
  }
  .contact-list {
    position: absolute;
    left: 292px;
    top: 178px;
    list-style: none;
    color: var(--muted);
    font-size: 12.5px;
    letter-spacing: 1px;
    line-height: 17px;
  }
  .contact-list li { display: flex; align-items: flex-start; margin-bottom: 7px; }
  .contact-icon { flex: none; width: 11px; height: 11px; margin: 3px 7px 0 0; }

  .back-brand {
    position: absolute;
    left: 0;
    right: 0;
    top: 92px;
    text-align: center;
    font-weight: 300;
    font-size: 62px;
    letter-spacing: 3px;
    color: var(--paper);
  }
  .back-web {
    position: absolute;
    left: 150px;
    top: 210px;
    font-weight: 700;
    font-size: 13px;
    letter-spacing: 1.5px;
    color: var(--paper);
  }
  .back-band {
    position: absolute;
    left: 0;
    right: 0;
    top: 234px;
    height: 12px;
    background: var(--paper);
  }
</style>
</head>
<body>
<main class="stage">

  <section class="card card-front" aria-label="Business card front">
    <svg class="card-shapes" width="520" height="300" viewBox="0 0 520 300">
      <polygon class="brand-panel" points="0,0 145,0 245,145 150,300 0,300" fill="var(--paper)"/>
      <polyline class="divider-stripe" points="172,-4 262,148 524,158" fill="none" stroke="var(--paper)" stroke-width="10" stroke-linejoin="miter"/>
    </svg>
    <div class="front-brand">KRT Design</div>
    <div class="holder-name">Your Name</div>
    <div class="holder-title">Designation</div>
    <ul class="contact-list">
      <li>
        <svg class="contact-icon" viewBox="0 0 12 12"><circle cx="6" cy="6" r="6" fill="var(--muted)"/><path d="M6 2.5a2.2 2.2 0 0 0-2.2 2.2C3.8 6.4 6 9.5 6 9.5s2.2-3.1 2.2-4.8A2.2 2.2 0 0 0 6 2.5z" fill="var(--ink)"/></svg>
        <span>111, Lorem Ipsum Street,<br>LW-123</span>
      </li>
      <li>
        <svg class="contact-icon" viewBox="0 0 12 12"><circle cx="6" cy="6" r="6" fill="var(--muted)"/><path d="M4 3l1.3 1.6-.7.9c.5.9 1 1.4 1.9 1.9l.9-.7L9 8l-.8 1C5.8 8.6 3.4 6.2 3 3.8z" fill="var(--ink)"/></svg>
        <span>123 456 789, 987 654 321</span>
      </li>
      <li>
        <svg class="contact-icon" viewBox="0 0 12 12"><circle cx="6" cy="6" r="6" fill="var(--muted)"/><rect x="3" y="4" width="6" height="4.2" fill="none" stroke="var(--ink)" stroke-width="0.9"/><path d="M3 4l3 2.3L9 4" fill="none" stroke="var(--ink)" stroke-width="0.9"/></svg>
        <span>yourmailid@krt.com</span>
      </li>
      <li>
        <svg class="contact-icon" viewBox="0 0 12 12"><circle cx="6" cy="6" r="6" fill="var(--muted)"/><circle cx="6" cy="6" r="3.2" fill="none" stroke="var(--ink)" stroke-width="0.9"/><path d="M2.8 6h6.4M6 2.8c-1.6 2-1.6 4.4 0 6.4M6 2.8c1.6 2 1.6 4.4 0 6.4" fill="none" stroke="var(--ink)" stroke-width="0.7"/></svg>
        <span>yourwebsitekrt.com</span>
      </li>
    </ul>
  </section>

  <section class="card card-back" aria-label="Business card back">
    <div class="back-brand">KRT Design</div>
    <div class="back-web">yourwebsitekrt.com</div>
    <div class="back-band"></div>
  </section>

</main>
</body>
</html>
```